Crestway screen porch

Can you please design a flyer for me promoting my screen porch businessPlease remove the seamless gutters word from the title and add “screen porches” I have added the logo and a bunch of pictures from projects that I have done in the past. You can use words like Hillcrest Screen porches, etc

Target Market(s)

homeowners, contractors, builders

Industry/Entity Type

Construction

Requirements
Must have
• Dom Karsten
• Crestway Gutters
• 2957 Old Hwy 38 N, Greer, SC 29873
• 864-555-0186
Nice to have
• A few colors maybe 3 most
• nice looking font

```html
<!DOCTYPE html>
<html lang="en">
<head>
<meta charset="utf-8">
<title>Crestway Screen Porches – Rack Card</title>
<link href="https://fonts.googleapis.com/css2?family=Oswald:wght@500;600&display=swap" rel="stylesheet">
<style>
  :root {
    --brand-red: #d3132f;
    --ink: #111111;
    --paper: #ffffff;
    --backdrop: #e6e6e6;
    --photo-sky: #b9c3c8;
    --photo-house: #c9c2ab;
    --photo-shade: #4d5650;
    --photo-lawn: #6f7d55;
  }
  * { margin: 0; padding: 0; box-sizing: border-box; }
  html, body { width: 1200px; height: 1000px; overflow: hidden; }
  body {
    background: var(--backdrop);
    font-family: "Oswald", "Arial Narrow", sans-serif;
    position: relative;
  }
  .rack-card {
    position: absolute;
    left: 370px; top: 40px;
    width: 460px; height: 920px;
    background: var(--paper);
    box-shadow: 0 2px 10px rgba(0,0,0,0.12);
    overflow: hidden;
  }
  .brand-name {
    position: absolute;
    left: 20px; right: 20px; top: 50px;
    text-align: center;
    color: var(--brand-red);
    font-weight: 600;
    line-height: 1;
    text-transform: uppercase;
  }
  .brand-name .primary { display: block; font-size: 96px; letter-spacing: 2px; }
  .brand-name .secondary { display: block; font-size: 40px; letter-spacing: 4px; margin-top: 20px; }
  .photo {
    position: absolute;
    background: linear-gradient(180deg, var(--photo-sky) 0%, var(--photo-house) 45%, var(--photo-shade) 75%, var(--photo-lawn) 100%);
  }
  .photo.hero {
    left: 30px; top: 300px; width: 196px; height: 230px;
    background: linear-gradient(160deg, #3b3a33 0%, #7b8279 40%, #b49a6c 80%, #8d7450 100%);
  }
  .headline {
    position: absolute;
    left: 240px; top: 304px; width: 196px;
    color: var(--brand-red);
    font-weight: 500;
    font-size: 42px;
    line-height: 1.2;
    letter-spacing: -0.5px;
    text-transform: uppercase;
  }
  .project-grid {
    position: absolute;
    left: 30px; top: 545px;
    width: 400px; height: 236px;
    display: grid;
    grid-template-columns: repeat(3, 1fr);
    grid-template-rows: repeat(2, 1fr);
    gap: 6px;
  }
  .project-grid .photo { position: static; }
  .project-grid .photo:nth-child(2) { background: linear-gradient(180deg, #cfd6da, #e9e7df 50%, #8f9a86); }
  .project-grid .photo:nth-child(3) { background: linear-gradient(180deg, #a9b4b8, #d2d0c6 50%, #7b7f72); }
  .project-grid .photo:nth-child(4) { background: linear-gradient(180deg, #8fa86a, #e2dcc2 45%, #9aa07c); }
  .project-grid .photo:nth-child(5) { background: linear-gradient(180deg, #9bb0c4, #4a4a7a 35%, #d7cfb6 65%, #7a5a4a); }
  .project-grid .photo:nth-child(6) { background: linear-gradient(180deg, #bfcad1, #596066 45%, #dcdcd6 70%, #7c8a58); }
  .contact-band {
    position: absolute;
    left: 30px; top: 795px;
    width: 400px; height: 105px;
    background: var(--brand-red);
    color: var(--paper);
    text-align: center;
    padding-top: 8px;
  }
  .contact-band .owner { font-size: 27px; font-weight: 500; line-height: 1.25; }
  .contact-band .address { font-size: 19px; font-weight: 500; line-height: 1.4; }
  .contact-band .phone {
    font-size: 21px; font-weight: 500; line-height: 1.3;
    display: inline-flex; align-items: center; gap: 8px;
  }
  .phone-icon { width: 20px; height: 20px; }
</style>
</head>
<body>
  <main class="rack-card">
    <h1 class="brand-name">
      <span class="primary">Crestway</span>
      <span class="secondary">Screen Porches</span>
    </h1>

    <div class="photo hero" role="img" aria-label="Photo of a finished screened porch with black railing and a screen door"></div>
    <h2 class="headline">Hillcrest<br>Screen<br>Porches</h2>

    <section class="project-grid" aria-label="Past projects">
      <div class="photo" role="img" aria-label="Photo of an elevated gabled screen porch"></div>
      <div class="photo" role="img" aria-label="Photo of a white-framed screen porch"></div>
      <div class="photo" role="img" aria-label="Photo of a screen porch with stairs"></div>
      <div class="photo" role="img" aria-label="Photo of a screen porch beside siding"></div>
      <div class="photo" role="img" aria-label="Photo of a raised screen porch on a deck"></div>
      <div class="photo" role="img" aria-label="Photo of a ground-level screen porch"></div>
    </section>

    <footer class="contact-band">
      <p class="owner">Dom Karsten • Crestway Gutters</p>
      <p class="address">2957 Old Hwy 38 N, Greer, SC 29873</p>
      <p class="phone">
        <svg class="phone-icon" viewBox="0 0 20 20" aria-hidden="true">
          <circle cx="10" cy="10" r="8.5" fill="none" stroke="#fff" stroke-width="1.6"/>
          <path d="M7 5.5 L8.6 7.6 L7.6 8.8 Q8.6 11.2 11 12.4 L12.3 11.4 L14.4 13 L13.4 14.5 Q8.5 14 5.6 7 Z" fill="#fff"/>
        </svg>
        864-555-0186
      </p>
    </footer>
  </main>
</body>
</html>
```